Calendar Ad / Flyer

Our law firm needs a calendar ad to place in a local calendar.
THE DEADLINE IS THIS THURSDAY 06/28/2018.

Attached is the ad used in last years calendar. A few notes on this...
**. This is by no means the model to follow.
Please be creative and do what makes more sense marketing wise.
1. Need to update the color scheme which corresponds to the new website at morvanlegal.net
2. The "MORVAN LEGAL | STANDING FIRM FOR YOUR FUTURE" should be put at the top and made larger
3. "KNOWN AND TRUSTED IN OUR COMMUNITY FOR OVER 21 YEARS" should be changed to "KNOWN AND TRUSTED IN OUR COMMUNITY FOR OVER 22 YEARS"
4. "Dorian K. Morvan, Esq." should be made larger and better positioned.
5. Under the list of practices, it should be changed to have:
"Personal Injury, Legal Malpractice, Unlicensed Contractors, Medical Malpractice, Civil Litigation"
6. Contact information (i.e. contact number, website, and address) should be better positioned
7. Placement of endorsement logos should stand out more.
8. New picture of head attorney is attached.

Last but not least... Give it your best shot!

```html
<!DOCTYPE html>
<html lang="en">
<head>
<meta charset="utf-8">
<title>Morvan Legal – Calendar Ad</title>
<link href="https://fonts.googleapis.com/css2?family=Playfair+Display:wght@700&family=Roboto:wght@400;500;700&display=swap" rel="stylesheet">
<style>
  :root {
    --page: #e4e4e6;
    --paper: #ffffff;
    --slate: #494c52;
    --night: #26272a;
    --gold: #c9a46c;
    --ink: #1d1d1d;
    --text: #333333;
    --muted: #555555;
    --badge-red: #8f1d22;
    --badge-blue: #1c5fa8;
    --badge-grey: #b9b1a2;
  }
  * { margin: 0; padding: 0; box-sizing: border-box; }
  html, body { width: 1200px; height: 1200px; overflow: hidden; background: var(--page); }
  .ad {
    position: absolute; left: 0; top: 136px;
    width: 1164px; height: 900px;
    transform: scale(1.0309); transform-origin: top left;
    background: var(--paper);
    font-family: "Roboto", Arial, sans-serif;
  }
  .ad-shapes { position: absolute; inset: 0; }
  .brand {
    position: absolute; right: 35px; top: 108px;
    display: flex; align-items: center; gap: 14px;
  }
  .brand-mark { width: 40px; height: 40px; background: var(--gold); }
  .brand-name {
    font-family: "Roboto", Arial, sans-serif; font-weight: 500;
    font-size: 50px; letter-spacing: 4px; color: var(--gold); line-height: 1;
  }
  .brand-tagline {
    position: absolute; right: 62px; top: 163px;
    font-weight: 700; font-size: 18px; letter-spacing: 0.5px; color: var(--muted);
  }
  .headline {
    position: absolute; left: 73px; top: 180px;
    font-family: "Playfair Display", Georgia, serif; font-weight: 700;
    font-size: 41px; line-height: 51px; color: #fff; letter-spacing: -0.5px;
  }
  .quote-mark {
    position: absolute; font-family: "Playfair Display", Georgia, serif;
    font-weight: 700; font-size: 64px; color: var(--gold); line-height: 1;
  }
  .quote-open { left: 33px; top: 168px; }
  .quote-close { left: 480px; top: 278px; }
  .practice-list {
    position: absolute; left: 52px; top: 350px; list-style: none;
  }
  .practice-list li {
    font-size: 32px; line-height: 51px; color: var(--gold);
    padding-left: 28px; position: relative;
  }
  .practice-list li::before {
    content: ""; position: absolute; left: 0; top: 22px;
    width: 10px; height: 10px; border-radius: 50%; background: var(--gold);
  }
  .contact-line {
    position: absolute; left: 33px; display: flex; align-items: center; gap: 25px;
    color: #fff;
  }
  .contact-phone { top: 676px; font-size: 44px; }
  .contact-web { top: 745px; font-size: 42px; }
  .contact-line svg { flex: none; }
  .address {
    position: absolute; left: 53px; top: 815px;
    display: flex; gap: 28px; font-size: 22px; line-height: 27px; color: var(--text);
  }
  .attorney-name {
    position: absolute; left: 460px; right: 0; top: 667px; height: 93px;
    display: flex; align-items: center; justify-content: center;
    font-family: "Playfair Display", Georgia, serif; font-weight: 700;
    font-size: 44px; color: var(--ink); padding-left: 20px;
  }
</style>
</head>
<body>
<main class="ad">
  <svg class="ad-shapes" width="1164" height="900" viewBox="0 0 1164 900" aria-hidden="false">
    <defs>
      <linearGradient id="skyline" x1="0" y1="0" x2="1" y2="1">
        <stop offset="0" stop-color="#2f3033"/>
        <stop offset="0.6" stop-color="#232426"/>
        <stop offset="1" stop-color="#1b1c1e"/>
      </linearGradient>
      <radialGradient id="portrait" cx="0.5" cy="0.55" r="0.55">
        <stop offset="0" stop-color="#8a8a8c"/>
        <stop offset="0.6" stop-color="#5b5c60"/>
        <stop offset="1" stop-color="#2a2b2e" stop-opacity="0"/>
      </radialGradient>
    </defs>
    <rect x="0" y="215" width="1164" height="452" fill="url(#skyline)" role="img" aria-label="Dark city skyline at night behind the attorney"/>
    <rect x="600" y="235" width="480" height="432" fill="url(#portrait)" role="img" aria-label="Portrait of attorney Dorian K. Morvan in a grey suit and blue tie"/>
    <polygon points="0,155 612,155 415,632 0,632" fill="var(--slate)"/>
    <polygon points="0,667 424,667 466,806 0,806" fill="var(--slate)"/>
    <polygon points="428,667 1164,667 1164,760 458,760" fill="var(--gold)"/>
    <g class="badges">
      <rect x="502" y="790" width="98" height="72" rx="6" fill="var(--badge-grey)"/>
      <rect x="637" y="790" width="118" height="80" rx="6" fill="var(--badge-red)"/>
      <circle cx="826" cy="828" r="42" fill="var(--badge-red)"/>
      <circle cx="945" cy="828" r="42" fill="var(--badge-blue)"/>
      <rect x="1035" y="785" width="94" height="85" rx="4" fill="var(--badge-blue)"/>
    </g>
  </svg>

  <header>
    <div class="brand">
      <span class="brand-mark"></span>
      <span class="brand-name">MORVAN LEGAL</span>
    </div>
    <p class="brand-tagline">STANDING FIRM FOR YOUR FUTURE</p>
  </header>

  <span class="quote-mark quote-open">“</span>
  <h1 class="headline">KNOWN AND TRUSTED<br>IN OUR COMMUNITY<br>FOR OVER 22 YEARS</h1>
  <span class="quote-mark quote-close">”</span>

  <ul class="practice-list">
    <li>Personal Injury</li>
    <li>Legal Malpractice</li>
    <li>Unlicensed Contractors</li>
    <li>Medical Malpractice</li>
    <li>Civil Litigation</li>
  </ul>

  <p class="contact-line contact-phone">
    <svg width="42" height="42" viewBox="0 0 24 24"><path fill="#fff" d="M6.6 10.8a15.2 15.2 0 0 0 6.6 6.6l2.2-2.2a1 1 0 0 1 1-.25 11.4 11.4 0 0 0 3.6.57 1 1 0 0 1 1 1V20a1 1 0 0 1-1 1A17 17 0 0 1 3 4a1 1 0 0 1 1-1h3.5a1 1 0 0 1 1 1c0 1.25.2 2.45.57 3.57a1 1 0 0 1-.25 1z"/></svg>
    (888) 555-0147
  </p>
  <p class="contact-line contact-web">
    <svg width="30" height="30" viewBox="0 0 24 24" fill="none" stroke="#fff" stroke-width="1.6"><circle cx="12" cy="12" r="10"/><ellipse cx="12" cy="12" rx="4.5" ry="10"/><path d="M2 12h20M4 7h16M4 17h16"/></svg>
    <span style="margin-left:12px">morvanlegal.net</span>
  </p>
  <address class="address" style="font-style:normal">
    <svg width="16" height="22" viewBox="0 0 16 22"><path fill="var(--text)" d="M8 0a8 8 0 0 0-8 8c0 6 8 14 8 14s8-8 8-14a8 8 0 0 0-8-8zm0 11a3 3 0 1 1 0-6 3 3 0 0 1 0 6z"/></svg>
    <span>2180 Larkfield Ave., Suite #405<br>Westbrook, CA 90318</span>
  </address>

  <p class="attorney-name">Dorian K. Morvan, Esq.</p>
</main>
</body>
</html>
```